Web Developer Needs a Business Card Design

I need a personal business card design that represents me as a web developer for potential employers. I would like the background to be a dark color on the front for contrast with my logo and name. The back will have all my information along with a smaller version of the logo. I want something with a modern look and feel, not too conservative. This will be used for potential employers and freelance work.

Industry/Entity Type

Business

Contact Information for Business Card

Front should have my logo and name. The back should have all my personal information which would include: name: Tom Brevardi, phone: 570-614-9083, email: tombrevardi@mailwisp.com, website url: www.tombrevardi.com, logo, web developer.

Font styles to use
Sans Serif

Requirements
Must have
• Must include my logo. The color palette base color will be the logo color.

```html
<!DOCTYPE html>
<html lang="en">
<head>
<meta charset="utf-8">
<title>Tom Brevardi – Business Card</title>
<link rel="stylesheet" href="https://fonts.googleapis.com/css2?family=Questrial&display=swap">
<style>
  :root {
    --stage: #3a3a3a;
    --teal: #4fd1b5;
    --teal-deep: #3fc2a6;
    --card-dark: #221b19;
    --card-light: #f6f6f4;
    --ink: #5a5a5a;
    --ink-soft: #8a8a8a;
    --band-gray: #555555;
    --white: #ffffff;
  }
  * { box-sizing: border-box; margin: 0; padding: 0; }
  html, body {
    width: 1200px; height: 768px; overflow: hidden;
    background: var(--stage);
    font-family: "Questrial", "Century Gothic", sans-serif;
  }
  .stage {
    position: relative; width: 1200px; height: 768px;
    display: flex; align-items: center; justify-content: center; gap: 40px;
  }
  .card {
    position: relative; width: 540px; height: 309px; overflow: hidden;
    border-radius: 3px;
    box-shadow: 0 10px 24px rgba(0,0,0,.35);
  }

  /* Front (dark) */
  .card--front { background: var(--card-dark); }
  .front-backdrop {
    position: absolute; inset: 0;
    background: linear-gradient(135deg, #2c2624 0%, #1d1715 55%, #2a2523 100%);
  }
  .front-content {
    position: relative; height: 100%;
    display: flex; flex-direction: column; align-items: center; justify-content: center;
  }
  .brand-mark { display: flex; align-items: center; gap: 10px; color: var(--teal); }
  .brand-mark__ring {
    width: 34px; height: 34px; border-radius: 50%;
    border: 5px solid var(--teal);
  }
  .brand-mark__name { font-size: 26px; letter-spacing: .5px; }
  .front-name {
    margin-top: 26px; color: var(--white);
    font-size: 26px; letter-spacing: 3px;
  }
  .front-title { margin-top: 6px; color: #b3b3b3; font-size: 13px; letter-spacing: 1px; }

  /* Back (light) */
  .card--back { background: var(--card-light); }
  .back-tab {
    position: absolute; left: 0; top: 22px; width: 8px; height: 30px;
    background: var(--band-gray);
  }
  .back-name { position: absolute; left: 34px; top: 22px; color: var(--teal); font-size: 22px; }
  .back-title { position: absolute; left: 34px; top: 50px; color: var(--ink); font-size: 14px; }
  .contact-list {
    position: absolute; left: 34px; top: 96px; list-style: none;
  }
  .contact-list li {
    display: flex; align-items: center; gap: 12px;
    color: var(--ink); font-size: 14px; height: 22px;
  }
  .contact-list svg { width: 14px; height: 14px; flex: none; }
  .back-mark {
    position: absolute; right: 34px; bottom: 52px;
    display: flex; align-items: center; gap: 10px; color: var(--teal);
  }
  .back-mark .brand-mark__ring { width: 52px; height: 52px; border-width: 6px; }
  .back-mark .brand-mark__name { font-size: 24px; }
  .band { position: absolute; bottom: 0; height: 22px; }
  .band--teal { left: 0; width: 68%; background: var(--teal-deep); }
  .band--gray { left: 68%; right: 0; background: var(--band-gray); }
</style>
</head>
<body>
<main class="stage">

  <section class="card card--front" aria-label="Card front">
    <div class="front-backdrop" role="img" aria-label="Dark desk photograph with a laptop, in deep brown tones"></div>
    <div class="front-content">
      <div class="brand-mark">
        <span class="brand-mark__ring"></span>
        <span class="brand-mark__name">Brevardi</span>
      </div>
      <h1 class="front-name">TOM BREVARDI</h1>
      <p class="front-title">Front-End Developer</p>
    </div>
  </section>

  <section class="card card--back" aria-label="Card back">
    <span class="back-tab"></span>
    <h2 class="back-name">Tom Brevardi</h2>
    <p class="back-title">Front-End Developer</p>
    <ul class="contact-list">
      <li>
        <svg viewBox="0 0 16 16" fill="var(--teal)"><path d="M4 1l3 3-1.5 2a9 9 0 0 0 4.5 4.5L12 9l3 3-2 3C7 15 1 9 1 3z"/></svg>
        570-614-9083
      </li>
      <li>
        <svg viewBox="0 0 16 16"><rect x="1" y="3" width="14" height="10" rx="1" fill="var(--teal)"/><path d="M1.5 4l6.5 5 6.5-5" stroke="#fff" stroke-width="1.3" fill="none"/></svg>
        tombrevardi@mailwisp.com
      </li>
      <li>
        <svg viewBox="0 0 16 16" fill="none" stroke="var(--teal)" stroke-width="1.5"><circle cx="8" cy="8" r="6.5"/><ellipse cx="8" cy="8" rx="2.8" ry="6.5"/><path d="M1.5 8h13"/></svg>
        www.tombrevardi.com
      </li>
      <li>
        <svg viewBox="0 0 16 16"><circle cx="8" cy="8" r="6.5" fill="var(--teal)"/></svg>
        @tombrevardi.com
      </li>
      <li>
        <svg viewBox="0 0 16 16"><rect x="1.5" y="1.5" width="13" height="13" fill="var(--teal)"/></svg>
        tombrevardi.com
      </li>
      <li>
        <svg viewBox="0 0 16 16"><circle cx="8" cy="8" r="6.5" fill="var(--teal)"/></svg>
        tombrevardi.com
      </li>
    </ul>
    <div class="back-mark brand-mark">
      <span class="brand-mark__ring"></span>
      <span class="brand-mark__name">Brevardi</span>
    </div>
    <span class="band band--teal"></span>
    <span class="band band--gray"></span>
  </section>

</main>
</body>
</html>
```